Sub-Antarctic Islands - Xmas and New Year 2020

I need to create a double sided A4 flyer that I will need to be able to have printed in colour and also email as an attachment.

My company is a Travel agency that packages flights/hotels/transfers&cruise and sells it as one price to the public.

Please see the attachment the email has a lot of info.

Target Market(s)

Bird Watchers

Industry/Entity Type

Travel Industry

Font styles to use
Sans Serif

Colors

Designer to choose colors to be used in the design.

Requirements
Must have
• VoyaMerry Logo
• Goldwake Logo
• Cruise Itinerary
• Inclusions in the package
• Costings
• Photo of one of the bird pictures and a penguin and or a seal
Nice to have
• A very professional appearance.
• A flyer that would make you want to call me to book
• Must be very clear to read as most buyers are seniors
• Please see the attachment the email has a lot of info.
Should not have
• any abbreviations

```html
<!DOCTYPE html>
<html lang="en">
<head>
<meta charset="utf-8">
<title>Sub Antarctic Islands Expedition Flyer</title>
<link rel="stylesheet" href="https://fonts.googleapis.com/css2?family=Montserrat:wght@400;500;600;700;800&display=swap">
<style>
  :root{
    --backdrop:#c1bdbd;
    --navy:#111848;
    --navy-deep:#0b1036;
    --cyan:#29abe2;
    --white:#ffffff;
    --text-soft:#e6e8f2;
  }
  *{box-sizing:border-box;margin:0;padding:0}
  html,body{width:1200px;height:840px;overflow:hidden}
  body{background:var(--backdrop);font-family:"Montserrat",Arial,sans-serif;color:var(--white);position:relative}
  .flyer-page{position:absolute;top:60px;width:509px;height:720px;background:var(--navy);overflow:hidden}
  .flyer-front{left:79px}
  .flyer-back{left:620px}
  .abs{position:absolute}

  /* front */
  .front-art{position:absolute;left:0;top:0}
  .offer-tagline{left:53px;top:483px;font-size:15.5px;font-weight:700;color:var(--cyan)}
  .fare-ribbon{left:0;top:509px;width:250px;height:36px;background:var(--cyan);clip-path:polygon(0 0,241px 0,250px 100%,0 100%);padding:3px 0 0 53px;font-size:9px;font-weight:700;line-height:9.6px}
  .trip-facts{left:253px;top:485px;font-size:9.7px;font-weight:700;line-height:11px}
  .trip-facts p+p{margin-top:6px}
  .trip-summary{left:46px;top:553px;width:418px;text-align:center;font-size:10px;line-height:12.3px;color:var(--text-soft)}

  /* footer shared */
  .brand-bar{left:0;top:620px;width:509px;height:41px;background:var(--white);display:flex;align-items:center}
  .brand-mark{display:flex;align-items:center;gap:5px;margin-left:45px;width:220px;color:var(--navy);font-size:16px;font-weight:800;letter-spacing:.2px}
  .brand-dot{width:14px;height:14px;border-radius:50%;background:var(--cyan)}
  .web-address{display:flex;align-items:center;gap:5px;color:var(--navy);font-size:14px;font-weight:700}
  .contact-row{left:0;top:666px;width:509px;font-size:9.6px;line-height:10.8px}
  .contact-prompt{left:53px;top:0}
  .contact-person{left:230px;top:0;width:150px;text-align:center;font-weight:700}
  .contact-email{left:352px;top:0}

  /* back */
  .intro-copy{left:39px;top:24px;width:431px;font-size:9.9px;line-height:12.3px;text-align:justify;color:var(--text-soft)}
  .photo-band{left:0;top:143px;width:509px;height:137px;display:flex}
  .photo-coast{width:333px;height:100%;background:linear-gradient(180deg,#8d9399 0%,#aab0b4 25%,#5f7482 45%,#4a5a3c 70%,#6b6a32 100%)}
  .photo-surf{flex:1;height:100%;background:linear-gradient(180deg,#6e7478 0%,#a9adb0 30%,#d8dbdc 55%,#8c8f90 80%,#5a5c5d 100%)}
  .highlight-band{left:0;top:280px;width:509px;height:67px;background:var(--cyan);padding:8px 40px 0 39px;font-size:9.3px;line-height:11.2px}
  .highlight-band p+p{margin-top:2px}
  .highlight-band strong{font-weight:700}
  .section-title{font-size:16px;font-weight:700;color:var(--cyan)}
  .inclusions-title{left:39px;top:356px}
  .inclusion-list{left:39px;top:380px;width:440px;list-style:none;font-size:9.3px;line-height:11.2px;color:var(--text-soft)}
  .costings-title{left:39px;top:543px}
  .costings-copy{left:39px;top:566px;width:435px;font-size:9.3px;line-height:11.4px;color:var(--text-soft)}
</style>
</head>
<body>

<section class="flyer-page flyer-front">
  <svg class="front-art" width="509" height="480" viewBox="0 0 509 480">
    <defs>
      <linearGradient id="shipScene" x1="0" y1="0" x2="0" y2="1">
        <stop offset="0" stop-color="#3f8fd6"/><stop offset=".45" stop-color="#8fb7d9"/>
        <stop offset=".62" stop-color="#6e6b6a"/><stop offset=".75" stop-color="#5d8fbf"/><stop offset="1" stop-color="#2d5f97"/>
      </linearGradient>
      <linearGradient id="albatrossNest" x1="0" y1="0" x2="1" y2="1">
        <stop offset="0" stop-color="#4e6a2e"/><stop offset=".5" stop-color="#e8ecea"/><stop offset="1" stop-color="#c9a52b"/>
      </linearGradient>
      <linearGradient id="penguinShore" x1="0" y1="0" x2="0" y2="1">
        <stop offset="0" stop-color="#8b8f92"/><stop offset=".5" stop-color="#d9dadb"/><stop offset="1" stop-color="#5d6063"/>
      </linearGradient>
      <linearGradient id="albatrossGrass" x1="0" y1="0" x2="1" y2="1">
        <stop offset="0" stop-color="#6e7a3a"/><stop offset=".6" stop-color="#b9b59a"/><stop offset="1" stop-color="#4f5c2a"/>
      </linearGradient>
    </defs>
    <polygon points="0,0 509,0 509,144 0,213" fill="url(#shipScene)" role="img" aria-label="Expedition ship anchored in a calm bay below snowy mountains"/>
    <polygon points="0,213 509,144 509,151 0,222" fill="var(--white)"/>
    <polygon points="0,222 164,199 179,326 0,351" fill="url(#albatrossNest)" role="img" aria-label="White albatross nesting among yellow flowers"/>
    <polygon points="164,199 375,170 389,297 179,326" fill="url(#penguinShore)" role="img" aria-label="Crested penguins walking on a grey beach"/>
    <polygon points="375,170 509,151 509,281 389,297" fill="url(#albatrossGrass)" role="img" aria-label="Albatross pair on a tussock hillside"/>
    <polygon points="0,351 509,281 509,289 0,360" fill="var(--white)"/>
    <polygon points="0,360 509,289 509,300 0,381" fill="var(--navy-deep)"/>
    <g font-family="Montserrat, Arial, sans-serif" font-weight="800" font-size="25" fill="#ffffff">
      <text transform="translate(53,385) rotate(-7.3)" textLength="424" lengthAdjust="spacingAndGlyphs">Bird Watching at Macquarie</text>
      <text transform="translate(53,413) rotate(-7.3)" textLength="323" lengthAdjust="spacingAndGlyphs">and the New Zealand</text>
      <text transform="translate(53,441) rotate(-7.3)" textLength="326" lengthAdjust="spacingAndGlyphs">Sub Antarctic Islands</text>
      <text transform="translate(53,469) rotate(-7.3)" textLength="163" lengthAdjust="spacingAndGlyphs">expedition</text>
    </g>
  </svg>

  <h2 class="abs offer-tagline">Fly Free | Stay Free</h2>
  <div class="abs fare-ribbon">VoyaMerry limited group fares<br>From $17,990 per person twin share.<br>Solo fares on application</div>
  <div class="abs trip-facts">
    <p>From 19 December 2020 to 04 January 2021<br>Total package dates. 17 days / 16 nights</p>
    <p>Departure Port : Dunedin<br>Arrival Port : Dunedin<br>Ship : Goldwake Explorer</p>
  </div>
  <p class="abs trip-summary">A unique cruise letting you explore the Sub Antarctic Islands of New Zealand, one of the least visited regions in the world. Skiff outings &amp; shore visits with your expedition team all included. Opportunities for hiking with guided walks on the Auckland Islands, Campbell Island and Macquarie Island, all of which are UNESCO World Heritage Sites.</p>

  <div class="abs brand-bar">
    <div class="brand-mark"><span class="brand-dot"></span>VOYAMERRY</div>
    <div class="web-address">
      <svg width="20" height="20" viewBox="0 0 20 20" fill="none" stroke="var(--cyan)" stroke-width="1.6"><circle cx="10" cy="10" r="8.5"/><ellipse cx="10" cy="10" rx="3.8" ry="8.5"/><path d="M1.5 10h17M3 5.5h14M3 14.5h14"/></svg>
      www.voyamerry.com.au
    </div>
  </div>
  <div class="abs contact-row">
    <p class="abs contact-prompt">For more information or to<br>make a booking please contact:</p>
    <p class="abs contact-person">Declan Harrow<br>1-300-555-014<br>VoyaMerry Pty Ltd</p>
    <p class="abs contact-email">declan@voyamerry.com.au</p>
  </div>
</section>

<section class="flyer-page flyer-back">
  <div class="abs intro-copy">
    <p>On this cruise aboard the Goldwake Explorer, VoyaMerry invites you to discover the primitive beauty of the Sub Antarctic Islands of New Zealand. Set sail on a 15-day expedition cruise and let yourself be dazzled by an exceptional itinerary, home to bountiful wildlife that is not found elsewhere.</p>
    <p>Often described as the “Galapagos of the Southern Ocean”, the Sub Antarctic Islands of New Zealand are among the best preserved environments on the planet. Isolated and wild, they are one those end-of-world places that have very few visitors and really do provide a total change of scenery.</p>
  </div>

  <div class="abs photo-band">
    <div class="photo-coast" role="img" aria-label="Green cliffs above a sheltered island bay under cloud"></div>
    <div class="photo-surf" role="img" aria-label="Penguins hopping through surf with a ship offshore"></div>
  </div>

  <div class="abs highlight-band">
    <p><strong>Wildlife:</strong> colonies of fur seals, elephant seals, king and yelloweyed penguins. A very wide variety of birds: Gibson’s albatross, giant petrels, Auckland shags and rorquals.</p>
    <p><strong>Landscapes:</strong> Beaches of black sand, cliffs and lush green prairies, contrasting with snow capped mountain chains with looking over glacial valleys fiords</p>
  </div>

  <h2 class="abs section-title inclusions-title">VoyaMerry Package Inclusions</h2>
  <ul class="abs inclusion-list">
    <li>Return economy class airfare including taxes from any Australian airport.</li>
    <li>2 nights Hotel accommodation with breakfast at the Harbourline Hotel in Dunedin.</li>
    <li>Private transfer from Dunedin airport to the hotel.</li>
    <li>14 night cruise in a midship outside cabin on Goldwake Explorer.</li>
    <li>Parka and Gum boots. Guided Skiff, land and sea tours, and shoreside activities led by the Expeditions Team</li>
    <li>Enrichment lectures by a highly qualified Expeditions Team</li>
    <li>Suite is serviced twice a day. Unlimited Free Wifi</li>
    <li>Choice of restaurants, open-seating dining-dine when and with whom you want</li>
    <li>Port charges</li>
    <li>All meals onboard with an Open Bar (except premium brands)</li>
    <li>24hour room service</li>
    <li>English speaking lecturer and Expedition team- this is very important.</li>
    <li>Extensions are also possible just ask.</li>
  </ul>

  <h2 class="abs section-title costings-title">Costings:</h2>
  <p class="abs costings-copy">$17,990.00 per person twin share in a Verandah Cabin. Deposit of $5000 per person twin share due 7 days after confirmation. Final payment will be due on or before Monday 5 th Nov 2018. All payments once made are non-refundable - comprehensive Travel Insurance must be taken out prior to paying your deposit.</p>

  <div class="abs brand-bar">
    <div class="brand-mark"><span class="brand-dot"></span>VOYAMERRY</div>
    <div class="web-address">
      <svg width="20" height="20" viewBox="0 0 20 20" fill="none" stroke="var(--cyan)" stroke-width="1.6"><circle cx="10" cy="10" r="8.5"/><ellipse cx="10" cy="10" rx="3.8" ry="8.5"/><path d="M1.5 10h17M3 5.5h14M3 14.5h14"/></svg>
      www.voyamerry.com.au
    </div>
  </div>
  <div class="abs contact-row">
    <p class="abs contact-prompt">For more information or to<br>make a booking please contact:</p>
    <p class="abs contact-person">Declan Harrow<br>1-300-555-014<br>VoyaMerry Pty Ltd</p>
    <p class="abs contact-email">declan@voyamerry.com.au</p>
  </div>
</section>

</body>
</html>
```